8-page brochure for laboratory equipment in the beverage can industry

We are a small company in the quality inspection and testing industry for beverage and food cans and are in need of a product brochure for one of our key products.The brochure should comprise of 8-pages. We will need both a print-ready format (which we would like to print on 2 double-sided A3 pages, then fold them), as well as an electronic version of the brochure (PDF). We also need to be able to make modifications to it, so we will need the open design file.We have corporate colors and fonts that will have to be used, which we will provide you with.The structure and content are defined, but we need some creative thinking to make it look great!

Target Market(s)

Beverage fillers

Font styles to use
Other font styles liked:
• Nexa Bold, Gotham Book, Calibri

Requirements
Must have
• Must be informative and look appealing.
• Must use the content from the Word document provided (better quality images will be provided if needed).
• Must use the company's corporate colors and fonts.
• Colors:
• Green: CMYK 99, 21, 86, 7
• Dark Grey: CMYK 67, 62, 58, 45
• Light Grey: CMYK 45, 36, 35, 1

```html
<!DOCTYPE html>
<html lang="en">
<head>
<meta charset="utf-8">
<title>Seam Inspection Brochure – Back and Front Cover</title>
<link href="https://fonts.googleapis.com/css2?family=Montserrat:wght@300;400;600;700;800&display=swap" rel="stylesheet">
<style>
  :root{
    --green:#1f9560;
    --green-light:#3fa877;
    --dark-grey:#564a4a;
    --light-grey:#8b8f92;
    --accent:#f2d22e;
    --white:#ffffff;
    --backdrop:#e4e5e6;
  }
  *{box-sizing:border-box;margin:0;padding:0}
  html,body{width:1200px;height:900px;overflow:hidden;background:var(--backdrop)}
  body{font-family:'Montserrat',sans-serif;color:var(--white)}
  .spread{position:absolute;left:40px;top:54px;width:1120px;height:792px;display:flex;box-shadow:0 6px 24px rgba(0,0,0,.18)}
  .page{position:relative;width:560px;height:792px;overflow:hidden}

  /* Back cover – FAQ */
  .faq{background:var(--green-light)}
  .faq-title{position:absolute;left:32px;top:34px;font-size:22px;font-weight:700;letter-spacing:.5px}
  .faq-columns{position:absolute;left:22px;top:80px;width:516px;display:flex;gap:14px}
  .faq-col{width:251px}
  .faq-item{margin-bottom:7px}
  .question{background:var(--dark-grey);font-size:8.4px;font-weight:700;line-height:1.3;padding:5px 8px 5px 20px;position:relative}
  .question::before{content:"";position:absolute;left:7px;top:7px;width:6px;height:6px;background:var(--accent)}
  .answer{list-style:none;padding:4px 6px 0 22px}
  .answer li{font-size:8px;line-height:1.32;position:relative;padding-left:9px;margin-bottom:2px;font-weight:400}
  .answer li::before{content:"";position:absolute;left:0;top:3px;border-left:5px solid var(--white);border-top:3px solid transparent;border-bottom:3px solid transparent}
  .answer li.sub{margin-left:10px}
  .answer li.sub::before{border-left-color:transparent;width:4px;height:4px;border:1px solid var(--white);top:2px}
  .faq-footer{position:absolute;left:0;bottom:0;width:100%;height:78px;background:var(--dark-grey);padding:14px 26px}
  .footer-web{font-size:8.5px;font-weight:700;letter-spacing:.4px;margin-bottom:6px}
  .contacts{display:flex;gap:18px}
  .contact{font-size:6.6px;line-height:1.45;width:118px}
  .contact strong{display:block;font-weight:700}

  /* Front cover */
  .cover{background:var(--white)}
  .cover-square{position:absolute;left:0;top:66px;width:122px;height:128px;background:var(--green)}
  .cover-title-band{position:absolute;left:140px;top:28px;right:0;height:150px;background:var(--dark-grey);padding:34px 24px 0 28px}
  .cover-title{font-size:23px;font-weight:800;line-height:1.15;letter-spacing:.3px}
  .cover-subtitle{margin-top:10px;font-size:12px;font-weight:300;color:#e6e1e1}
  .product-photo{position:absolute;left:96px;top:198px;right:0;height:430px;background:linear-gradient(180deg,#e9e9ea 0%,#b4b6b8 45%,#d9dadb 100%)}
  .cover-web{position:absolute;right:26px;top:600px;font-size:11px;font-weight:400;color:var(--dark-grey)}
  .cover-wave{position:absolute;left:0;top:610px;width:560px;height:110px}
  .brand{position:absolute;right:48px;top:724px;text-align:right}
  .brand-name{font-size:28px;font-weight:800;color:var(--dark-grey);letter-spacing:1px}
  .brand-tagline{font-size:8px;font-weight:400;color:var(--light-grey);letter-spacing:1px;margin-top:2px}
</style>
</head>
<body>
<div class="spread">

  <section class="page faq">
    <h2 class="faq-title">FREQUENTLY ASKED QUESTIONS</h2>
    <div class="faq-columns">
      <div class="faq-col">
        <div class="faq-item">
          <p class="question">Why is it important we measure tightness?</p>
          <ul class="answer"><li>XXX</li></ul>
        </div>
        <div class="faq-item">
          <p class="question">How do results compare to traditional cross section measurements?</p>
          <ul class="answer">
            <li>With our X-ray method, we create a virtual seam image based on the overlapping materials in the seam captured by the x-ray. We looking through the seam at the material distribution.</li>
            <li>With the traditional, destructive method, the seam is cut open and we look at the seam from a 90° angle. This means looking on the seam, as opposed to through the seam.</li>
            <li>The non-destructive method is more accurate as the seam is not affected by influence of force (e.g. saw blades pressure).</li>
          </ul>
        </div>
        <div class="faq-item">
          <p class="question">Define what is considered a “good”, “acceptable”, “bad” tightness rating? Show examples of good and bad cans (30%, 60%, 100% tightness?)</p>
          <ul class="answer"><li>XXX</li></ul>
        </div>
        <div class="faq-item">
          <p class="question">Which kinds of wrinkles and seam anomalies exist?</p>
          <ul class="answer"><li>Leaky can, false seam, ghost wrinkles, etc.</li></ul>
        </div>
        <div class="faq-item">
          <p class="question">Which cans can be measured?</p>
          <ul class="answer">
            <li>Round cans with the combination aluminium can and aluminium end, i.e. mostly beverage cans</li>
            <li>Round cans with steel cans and steel ends, i.e. mostly food cans</li>
            <li>Alu / steel combination for cross section only (not for wrinkle)</li>
            <li>Can sizes from diameter 40 mm to 153 mm, all can heights</li>
          </ul>
        </div>
        <div class="faq-item">
          <p class="question">What can sizes can be measured with the CANVIEW XR?</p>
          <ul class="answer"><li>All can sizes ranging from 40 mm to 153 mm diameter can be measured, and heights ranging from 12 mm to 240 mm</li></ul>
        </div>
      </div>

      <div class="faq-col">
        <div class="faq-item">
          <p class="question">How long does it take to measure one can? What is the speed?</p>
          <ul class="answer">
            <li>Between 80 and 210 sec, depending on the diameter of the can:</li>
            <li class="sub">45 sec for 52mm end (202) – 3 positions, cross section and wrinkle (202)</li>
            <li class="sub">80 sec per 200 diameter end – for consistency</li>
            <li class="sub">210 sec per 609 diameter end</li>
          </ul>
        </div>
        <div class="faq-item">
          <p class="question">Is it possible to integrate the device into a filling line?</p>
          <ul class="answer"><li>Yes, the AUTO-XR can be place on-line with an infeed and outfeed of a number of cans for testing</li></ul>
        </div>
        <div class="faq-item">
          <p class="question">What is the maximum weight of a can to be measured?</p>
          <ul class="answer"><li>5 kg</li></ul>
        </div>
        <div class="faq-item">
          <p class="question">Does the CANVIEW XR need to be placed in a laboratory environment?</p>
          <ul class="answer"><li>The gauge should be placed in an appropriate location, such as a laboratory</li></ul>
        </div>
        <div class="faq-item">
          <p class="question">How do you calibrate?</p>
          <ul class="answer">
            <li>Initial calibration while set-up by SEAMTEK for cross-section measurement.</li>
            <li>Wrinkle calibration can be done manually or automatically by the administrator locally.</li>
          </ul>
        </div>
        <div class="faq-item">
          <p class="question">How often to you calibrate?</p>
          <ul class="answer">
            <li>Suggested calibration of cross-section measurement by SEAMTEK technician annually and after repairs</li>
            <li>Wrinkle: After any seaming process changes (when changing the can type, end type, seamer adjustment tooling, etc.)</li>
          </ul>
        </div>
        <div class="faq-item">
          <p class="question">How easy is it to set up a new can?</p>
          <ul class="answer">
            <li>The supervisor, who has been trained by a SEAMTEK technician, can set up a new can</li>
            <li>For large changes in the geometry of the seam, SEAMTEK supports, either remotely or on-site.</li>
          </ul>
        </div>
      </div>
    </div>

    <footer class="faq-footer">
      <p class="footer-web">WWW.SEAMTEK-EXAMPLE.COM</p>
      <div class="contacts">
        <p class="contact"><strong>GERMANY</strong>Tel. +49 30 5550 1100<br>sales@seamtek-example.de</p>
        <p class="contact"><strong>UNITED STATES</strong>Tel. +1 555 010 2200<br>sales@seamtek-example.com</p>
        <p class="contact"><strong>MEXICO</strong>Tel. +52 55 5550 3300<br>sales@seamtek-example.mx</p>
        <p class="contact"><strong>CHINA</strong>Tel. +86 555 010 4400<br>china@seamtek-example.com</p>
      </div>
    </footer>
  </section>

  <section class="page cover">
    <div class="cover-square"></div>
    <header class="cover-title-band">
      <h1 class="cover-title">NON-DESTRUCTIVE SEAM<br>INSPECTION SYSTEMS</h1>
      <p class="cover-subtitle">CANVIEW XR III &amp; AUTO XR</p>
    </header>
    <div class="product-photo" role="img" aria-label="Photo of two stainless steel X-ray seam inspection machines with touch screens, a benchtop unit above and a conveyor-fed inline unit below"></div>
    <svg class="cover-wave" viewBox="0 0 560 110" preserveAspectRatio="none" aria-hidden="true">
      <path d="M0 62 C150 40 330 26 560 0 L560 40 C330 62 160 82 0 110 Z" fill="var(--green)"/>
    </svg>
    <p class="cover-web">www.seamtek-example.com</p>
    <div class="brand">
      <p class="brand-name">SEAMTEK</p>
      <p class="brand-tagline">QUALITY | ACCURACY | RELIABILITY</p>
    </div>
  </section>

</div>
</body>
</html>
```